Young Accounting firm needing a captivating business card

We need a business card design that forces the person to look at the card because its either gold foil, plastic, or lettering pop up etc. We already have a logo with a specific gold color and we need to make it pop. We are an accounting firm. I need the words" accounting, payroll, licenses, audits, taxes" somewhere on the business card so as to describe what we do- preferably on the side where the logo is at.

Industry/Entity Type

Accounting

Contact Information for Business Card

Address 48276 9th Ave S Ste 305, Federal Way, WA 98117
Business Phone (360)418-2096
Fax (360)418-2157
Office Cell Phone (360)586-7319

Font styles to use
Serif

Colors
85abd2

Requirements
Must have
• It should state
• "Accounting" "Taxes" "Audits" "Licenses" "Payroll"
Nice to have
• Matte with gold foil, different textures, With Either a textured ivory background or gray blue slate background
Should not have
• colorful colors

```html
<!DOCTYPE html>
<html lang="en">
<head>
<meta charset="utf-8">
<title>Halvane Ledger – Business Card</title>
<link href="https://fonts.googleapis.com/css2?family=Josefin+Sans:wght@200;300;400;600&display=swap" rel="stylesheet">
<style>
  :root {
    --page-bg: #efefef;
    --card-ivory: #fffbef;
    --honeycomb-tone: #fdf6e2;
    --band-bronze: #b5883f;
    --gold-deep: #c9a43c;
    --gold-bright: #dfc359;
    --gold-text: #d2b04a;
  }
  * { margin: 0; padding: 0; box-sizing: border-box; }
  html, body {
    width: 1200px; height: 1200px; overflow: hidden;
    background: var(--page-bg);
    font-family: "Josefin Sans", sans-serif;
  }
  .card {
    position: absolute; left: 204px;
    width: 792px; height: 484px;
    border-radius: 44px; overflow: hidden;
  }
  .card--front { top: 81px; }
  .card--back { top: 635px; }
  .card__texture {
    position: absolute; inset: 0;
    background: linear-gradient(135deg, var(--card-ivory), var(--honeycomb-tone));
  }
  .card__band {
    position: absolute; top: 53px; width: 15px; height: 375px;
    background: var(--band-bronze);
  }
  .card__band--left { left: 0; border-radius: 0 15px 15px 0; }
  .card__band--right { right: 0; border-radius: 15px 0 0 15px; }

  .brand {
    position: absolute; color: var(--gold-bright);
    font-weight: 400; letter-spacing: -0.5px; white-space: nowrap;
  }
  .brand--corner { right: 48px; top: 72px; font-size: 29px; }
  .brand--hero { left: 0; right: 0; top: 272px; text-align: center; font-size: 62px; }

  .person__name {
    position: absolute; left: 71px; top: 146px;
    font-size: 64px; font-weight: 600; letter-spacing: 1px;
    color: var(--gold-deep);
  }
  .person__title {
    position: absolute; left: 105px; top: 203px;
    font-size: 38px; font-weight: 200; color: var(--gold-deep);
  }
  .contact {
    position: absolute; left: 73px; top: 336px; list-style: none;
  }
  .contact__item {
    display: flex; align-items: center; height: 23.2px;
    font-size: 14.5px; letter-spacing: 0.6px; color: var(--gold-text);
  }
  .contact__icon { width: 15px; height: 15px; margin-right: 10px; fill: var(--gold-deep); }

  .services {
    position: absolute; left: 0; right: 0; top: 412px;
    text-align: center; font-size: 26px; font-weight: 400;
    letter-spacing: 1px; color: var(--gold-text);
  }
</style>
</head>
<body>

<section class="card card--front">
  <div class="card__texture" role="img" aria-label="Faint ivory honeycomb texture"></div>
  <div class="card__band card__band--left"></div>
  <div class="card__band card__band--right"></div>

  <div class="brand brand--corner">Halvane Ledger</div>

  <h1 class="person__name">DANIEL REYES</h1>
  <p class="person__title">Senior Accountant</p>

  <ul class="contact">
    <li class="contact__item">
      <svg class="contact__icon" viewBox="0 0 16 16"><path d="M8 0a5.5 5.5 0 0 0-5.5 5.5C2.5 10 8 16 8 16s5.5-6 5.5-10.5A5.5 5.5 0 0 0 8 0zm0 8a2.5 2.5 0 1 1 0-5 2.5 2.5 0 0 1 0 5z"/></svg>
      Address: 48276 9th Ave S Ste 305, Federal Way, WA 98117
    </li>
    <li class="contact__item">
      <svg class="contact__icon" viewBox="0 0 16 16"><path d="M3.6 1 6 3.8 4.7 5.6a9 9 0 0 0 5.7 5.7l1.8-1.3L15 12.4 13.3 15C6.5 14.6 1.4 9.5 1 2.7z"/></svg>
      Business Phone: (360)418-2096
    </li>
    <li class="contact__item">
      <svg class="contact__icon" viewBox="0 0 16 16"><rect x="0" y="5" width="4" height="11" rx="1"/><rect x="5" y="4" width="11" height="12" rx="1"/><rect x="7" y="0" width="7" height="4"/><rect x="7" y="7" width="2" height="2" fill="#fffbef"/><rect x="11" y="7" width="2" height="2" fill="#fffbef"/><rect x="7" y="11" width="2" height="2" fill="#fffbef"/><rect x="11" y="11" width="2" height="2" fill="#fffbef"/></svg>
      Fax: (360)418-2157
    </li>
    <li class="contact__item">
      <svg class="contact__icon" viewBox="0 0 16 16"><path d="M4 0h8a1.5 1.5 0 0 1 1.5 1.5v13A1.5 1.5 0 0 1 12 16H4a1.5 1.5 0 0 1-1.5-1.5v-13A1.5 1.5 0 0 1 4 0zm.5 1.5v11h7v-11zM8 13.3a.8.8 0 1 0 0 1.6.8.8 0 0 0 0-1.6z"/></svg>
      Office Cell Phone: (360)586-7319
    </li>
    <li class="contact__item">
      <svg class="contact__icon" viewBox="0 0 16 16"><path d="M0 3h16v10H0zm1.5 1.5v.3L8 9l6.5-4.2v-.3zm0 2.1v4.9h13V6.6L8 10.8z"/></svg>
      Email: daniel@halvaneledger.com
    </li>
  </ul>
</section>

<section class="card card--back">
  <div class="card__texture" role="img" aria-label="Faint ivory honeycomb texture"></div>
  <div class="card__band card__band--left"></div>
  <div class="card__band card__band--right"></div>

  <div class="brand brand--hero">Halvane Ledger</div>

  <p class="services">"Accounting - Taxes - Audits - Licenses - Payroll"</p>
</section>

</body>
</html>
```